Business card design needed for Automotive Reconditioning business

I have a logo design i just cant decide on the best color or layout for the business card, I will upload all the files so you can see all colors schemes we are considering. I have other file formats if needed let me know.

Target Market(s)

automotive dealerships

Contact Information for Business Card

HERE are the Descriptions and info needed on the card:
Interior Repair: Leather carpet burns panels dash Deoderize
Dealer products and Vin Verify
( spot for name and cell number) My name is Norman Bexley phone 614 352-4180 Title COO www.QuorvalMotive.com

Font styles to use
Sans Serif
Other font styles liked:
• what ever you think looks best

Requirements
Must have
• Must be able to change the name and phone for employees

```html
<!DOCTYPE html>
<html lang="en">
<head>
<meta charset="utf-8">
<title>Quorval Motive Reconditioning Corp. – Business Cards</title>
<link rel="stylesheet" href="https://fonts.googleapis.com/css2?family=Open+Sans:wght@400;600;700&display=swap">
<style>
  :root {
    --backdrop: #2e2a28;
    --card: #1d1c1d;
    --brand-blue: #1f86d6;
    --accent-red: #e8371f;
    --text-grey: #b9b9b9;
    --rule: #4a4a4a;
  }
  * { margin: 0; padding: 0; box-sizing: border-box; }
  html, body {
    width: 1200px; height: 844px; overflow: hidden;
    background: var(--backdrop);
    font-family: "Open Sans", Arial, sans-serif;
  }
  .card-set {
    position: absolute; inset: 0;
    display: flex; align-items: center; justify-content: center; gap: 44px;
  }
  .card {
    width: 520px; height: 300px;
    background: var(--card);
    box-shadow: 0 18px 40px rgba(0,0,0,.45);
    display: flex; flex-direction: column; align-items: center; justify-content: center;
    text-align: center;
  }
  .brand {
    display: flex; align-items: center; gap: 10px;
    font-weight: 700; font-size: 24px; letter-spacing: .5px;
    color: var(--brand-blue); text-transform: uppercase;
  }
  .brand-mark { width: 14px; height: 14px; background: var(--brand-blue); }
  .brand-sub {
    margin-top: 4px; font-size: 12px; font-weight: 700; letter-spacing: 1.5px;
    color: var(--brand-blue); text-transform: uppercase;
  }
  .person-name {
    margin-top: 22px; font-size: 18px; color: var(--accent-red);
    text-transform: uppercase; letter-spacing: .5px;
  }
  .person-title { font-size: 12px; color: var(--text-grey); }
  .rule { width: 150px; height: 1px; background: var(--rule); margin: 12px 0 10px; }
  .card-back .rule { width: 210px; margin: 18px 0 12px; }
  .contact { font-size: 15px; color: var(--text-grey); line-height: 1.35; }
  .services {
    max-width: 230px; font-size: 13px; line-height: 1.4; color: var(--text-grey);
  }
  .services-label { color: var(--accent-red); }
</style>
</head>
<body>
  <main class="card-set">
    <section class="card card-front">
      <div class="brand"><span class="brand-mark"></span>Quorval Motive</div>
      <div class="brand-sub">Reconditioning Corp.</div>
      <p class="person-name">Norman Bexley</p>
      <p class="person-title">CEO</p>
      <div class="rule"></div>
      <p class="contact">614 352-4180<br>www.QuorvalMotive.com</p>
    </section>
    <section class="card card-back">
      <div class="brand"><span class="brand-mark"></span>Quorval Motive</div>
      <div class="brand-sub">Reconditioning Corp.</div>
      <div class="rule"></div>
      <p class="services"><span class="services-label">Interior Repair:</span> Leather carpet burns panels dash Deoderize Dealer products and Vin Verify</p>
    </section>
  </main>
</body>
</html>
```